Natural Sunscreen Label Design for a Natural Cosmetics brand

We are looking to create a label design for a Natural Sunscreen Lotion. The labels will be a stick-on label on a white background tube. Enclosed a file with the content and some ideas/references. Please feel free to explore more.

It is important that the SPF is highlighted as large text and to use colors that give the customer an impression this being a sunscreen from far away as well.
We like white and orange/amber/yellow.
Details attached
Our Logo is attached as well as the size template of the label.

```html
<!DOCTYPE html>
<html lang="en">
<head>
<meta charset="utf-8">
<title>Natural Sun Lotion Label</title>
<link href="https://fonts.googleapis.com/css2?family=Oswald:wght@500;600&family=Montserrat:wght@700;800&family=Open+Sans:wght@400;600&family=Lobster+Two:ital,wght@1,700&display=swap" rel="stylesheet">
<style>
  :root {
    --page: #ebebeb;
    --label-white: #ffffff;
    --gold: #d4a51c;
    --gold-deep: #c8900f;
    --gold-light: #e9c24a;
    --gold-soft: #e3c568;
    --ink: #1b1b1b;
    --ink-grey: #6e6e6e;
    --leaf: #3d8b2e;
  }
  html, body {
    margin: 0;
    width: 1200px;
    height: 1200px;
    overflow: hidden;
    background: var(--page);
  }
  .label {
    position: absolute;
    left: 320px;
    top: 70px;
    width: 560px;
    height: 1060px;
    background: var(--label-white);
    border-radius: 6px;
    overflow: hidden;
    box-shadow: 0 2px 10px rgba(0,0,0,0.06);
  }
  .label-top {
    position: absolute;
    left: 0; top: 0;
    width: 100%;
    height: 420px;
    background: linear-gradient(90deg, var(--gold-light) 0%, var(--gold) 45%, var(--gold-deep) 100%);
  }
  .brand {
    position: absolute;
    left: 0; top: 130px;
    width: 100%;
    text-align: center;
    color: var(--label-white);
    font-family: "Montserrat", sans-serif;
    font-weight: 700;
    font-size: 15px;
    letter-spacing: 4px;
  }
  .brand-dot {
    display: block;
    width: 40px; height: 40px;
    margin: 0 auto 10px;
    border: 2px solid var(--label-white);
    border-radius: 50%;
  }
  .spf-badge {
    position: absolute;
    left: 160px; top: 300px;
    width: 240px; height: 240px;
  }
  .spf-text {
    position: absolute;
    left: 160px; top: 300px;
    width: 240px; height: 240px;
    color: var(--label-white);
    font-family: "Montserrat", sans-serif;
    font-weight: 800;
    text-align: center;
  }
  .spf-text .spf-word { position: absolute; left: 0; right: 0; top: 58px; font-size: 44px; }
  .spf-text .spf-value { position: absolute; left: 0; right: 0; top: 98px; font-size: 86px; line-height: 1; letter-spacing: -2px; }
  .spf-text .spf-plus { position: absolute; left: 172px; top: 84px; font-size: 40px; }
  .line-name {
    position: absolute;
    left: 112px; top: 610px;
    font-family: "Lobster Two", cursive;
    font-style: italic;
    font-weight: 700;
    font-size: 40px;
    color: var(--gold-soft);
  }
  .title {
    position: absolute;
    left: 110px;
    margin: 0;
    font-family: "Oswald", sans-serif;
    font-weight: 600;
    text-transform: uppercase;
    line-height: 1;
    background: linear-gradient(90deg, var(--ink-grey), var(--ink));
    -webkit-background-clip: text;
    background-clip: text;
    color: transparent;
  }
  .title-natural { top: 660px; font-size: 68px; }
  .title-lotion { top: 738px; font-size: 86px; letter-spacing: -1px; }
  .subtitle {
    position: absolute;
    left: 112px; top: 842px;
    font-family: "Oswald", sans-serif;
    font-weight: 500;
    font-size: 34px;
    color: var(--gold);
    line-height: 1;
  }
  .uv {
    position: absolute;
    left: 112px; top: 884px;
    font-family: "Montserrat", sans-serif;
    font-weight: 800;
    font-size: 28px;
    color: var(--ink);
    line-height: 1;
  }
  .use-band {
    position: absolute;
    left: 112px; top: 928px;
    width: 282px; height: 40px;
    background: var(--gold);
    color: var(--label-white);
    font-family: "Open Sans", sans-serif;
    font-size: 22px;
    line-height: 40px;
    padding-left: 8px;
    box-sizing: border-box;
  }
  .benefits {
    position: absolute;
    left: 112px; top: 980px;
    width: 340px;
    margin: 0;
    font-family: "Open Sans", sans-serif;
    font-size: 16px;
    line-height: 1.3;
    color: var(--ink);
  }
  .volume {
    position: absolute;
    left: 0; top: 1030px;
    width: 100%;
    text-align: center;
    font-family: "Open Sans", sans-serif;
    font-weight: 600;
    font-size: 20px;
    color: var(--ink);
  }
  .vegan-mark {
    position: absolute;
    left: 408px; top: 830px;
    width: 76px; height: 76px;
    border: 2px dashed var(--ink-grey);
    border-radius: 50%;
    box-sizing: border-box;
  }
</style>
</head>
<body>
  <main class="label">
    <div class="label-top"></div>

    <div class="brand"><span class="brand-dot"></span>COSTA AUREA · PORTUGAL</div>

    <svg class="spf-badge" viewBox="0 0 240 240" aria-hidden="true">
      <path d="M 6 120 A 114 114 0 0 1 234 120" fill="none" stroke="var(--label-white)" stroke-width="14" stroke-dasharray="170 12"/>
      <path d="M 234 120 A 114 114 0 0 1 6 120" fill="none" stroke="var(--gold-light)" stroke-width="14" stroke-dasharray="170 12"/>
      <circle cx="120" cy="120" r="100" fill="var(--gold-deep)"/>
    </svg>
    <div class="spf-text">
      <span class="spf-word">SPF</span>
      <span class="spf-value">30</span>
      <span class="spf-plus">+</span>
    </div>

    <div class="line-name">Marebrisa</div>
    <h1 class="title title-natural">Natural</h1>
    <h1 class="title title-lotion">Sun Lotion</h1>
    <div class="subtitle">PROTETOR SOLAR</div>
    <div class="uv">UVA &amp; UVB</div>
    <div class="vegan-mark"></div>
    <div class="use-band">For Body and Face</div>
    <p class="benefits">With BIO Aloe Vera, Non-greasy, Water Resistant, Safe for kids and adults</p>
    <div class="volume">100ml</div>
  </main>
</body>
</html>
```